Bravados- Tattoos/Piercings/Motorcycle/Biker Appearl Shop

Bravados' buisness cards can be creative, playful and eye catching. Incorporate leather or diamond plate. We are an all female business. Biker theme, Tattoo Photos, Piercing Photos, Diamond plate, Leather and Girls!

This project needs to be an appointment card as well for the tattoo artists and piercers. We need a section that says APPT With: _______ , DATE, TIME, and then a QUOTE and DEPOSIT section for the artists. I attached the logo so you could incorportate that and have complete creative freedom. It's a biker store, we sell biker appearl and accessories, with a tattoo and piercing shop connected. Girls, Leather, Tattoos and Piercings. Have fun with it!

I've Updated project details for better description of what im looking for. Thanks!

Target Market(s)

Male and Female Ages 15-90. Interests in custom tattoos and quality piercings, bikers, motorcycle accessories like helmets, gloves, masks, leather, boots. Jewlery and clothes.

Industry/Entity Type

Business

Contact Information for Business Card

The business is called Bravados, address, phone number and website. (2837 Wexley Ave. Muskegon, MI. 49517 (231)472-9035 www.inkridgeparlor.com)

Font styles to use
Serif
Sans Serif
Decorative
Script

Requirements
Must have
• Appointment with______
• Date_____ or MON TUES WED THUR etc... check mark boxes
• Time_____
• Quote______
• Deposit_______
• (231) 472-9035
• 2837 Wexley Ave
• Muskegon, MI 49517
• a facebook logo
Nice to have
• Owner Rick Hollowell
Should not have
• Tribal dragons or anything Tribal.That's cheesy! No Butterflies, No stars. No boys,

```html
<!DOCTYPE html>
<html lang="en">
<head>
<meta charset="utf-8">
<title>Bravados Appointment Card</title>
<link rel="stylesheet" href="https://fonts.googleapis.com/css2?family=Almendra+SC&family=Open+Sans:wght@700&display=swap">
<style>
  :root {
    --ink: #1a1410;
    --wine: #4e0d0e;
    --wine-deep: #2a0506;
    --parchment: #efe6c6;
    --parchment-warm: #d9c78e;
    --olive-shadow: #4a4420;
    --pillar-dark: #1d1b1a;
    --pillar-mid: #4a4744;
    --phone-red: #e3232a;
    --web-green: #72c04c;
    --silver: #d8d8d8;
    --gold: #f1e3c4;
  }
  html, body { margin: 0; padding: 0; overflow: hidden; background: #000; }
  .card {
    position: relative;
    width: 686px;
    height: 1200px;
    overflow: hidden;
    background:
      radial-gradient(ellipse 62% 48% at 50% 62%, var(--parchment) 0%, var(--parchment-warm) 55%, var(--olive-shadow) 92%, #141208 100%);
    font-family: "Almendra SC", serif;
    color: var(--ink);
  }
  .header-band {
    position: absolute; left: 0; top: 0; width: 686px; height: 420px;
    background: linear-gradient(180deg, var(--wine-deep) 0%, var(--wine) 30%, rgba(120,70,30,0.55) 70%, rgba(200,170,110,0) 100%);
  }
  .vignette {
    position: absolute; inset: 0;
    background: radial-gradient(ellipse 70% 62% at 50% 55%, rgba(0,0,0,0) 60%, rgba(0,0,0,0.85) 100%);
  }
  .pillar {
    position: absolute; top: 0; width: 82px; height: 610px;
    background: linear-gradient(90deg, var(--pillar-dark), var(--pillar-mid) 50%, var(--pillar-dark));
  }
  .pillar--left { left: 0; }
  .pillar--right { right: 0; }
  .brand-name {
    position: absolute; left: 0; right: 0; top: 92px;
    text-align: center;
    font-size: 104px; line-height: 1;
    color: var(--gold);
    margin: 0;
  }
  .machines-art {
    position: absolute; left: 212px; top: 263px; width: 270px; height: 195px;
    background: radial-gradient(ellipse at center, var(--silver) 0%, #8e8e8e 55%, rgba(60,50,40,0) 75%);
    border-radius: 20px;
  }
  .appt-heading {
    position: absolute; left: 0; right: 0; top: 488px;
    text-align: center; font-size: 40px; margin: 0; letter-spacing: 1px;
  }
  .appt-line {
    position: absolute; left: 183px; top: 594px; width: 341px; border-bottom: 2px solid var(--ink);
  }
  .field {
    position: absolute; left: 86px; width: 520px; height: 50px;
  }
  .field-label { position: absolute; left: 0; bottom: 0; font-size: 40px; line-height: 1; }
  .field-line { position: absolute; left: 196px; right: 0; bottom: 4px; border-bottom: 2px solid var(--ink); }
  .field--date { top: 652px; }
  .field--time { top: 720px; }
  .field--quote { top: 788px; }
  .field--deposit { top: 856px; }
  .social-mark {
    position: absolute; left: 320px; top: 948px; width: 27px; height: 27px;
    background: #3b5998; border-radius: 3px;
  }
  .contact { font-family: "Open Sans", sans-serif; font-weight: 700; position: absolute; left: 0; right: 0; text-align: center; margin: 0; }
  .phone { top: 1000px; font-size: 42px; color: var(--phone-red); }
  .rule { position: absolute; left: 80px; right: 80px; border-top: 1px dotted rgba(40,30,10,0.5); }
  .rule--top { top: 1058px; }
  .rule--bottom { top: 1122px; }
  .address { top: 1076px; font-size: 22px; color: var(--ink); }
  .website { top: 1138px; font-size: 27px; color: var(--web-green); }
</style>
</head>
<body>
  <main class="card">
    <div class="header-band" role="img" aria-label="Dark red backdrop with faint crown and diamond lattice pattern"></div>
    <div class="vignette"></div>
    <div class="pillar pillar--left" role="img" aria-label="Carved stone column wrapped by a sculpted dragon"></div>
    <div class="pillar pillar--right" role="img" aria-label="Carved stone column wrapped by a sculpted dragon"></div>

    <h1 class="brand-name">Bravados</h1>
    <div class="machines-art" role="img" aria-label="Two crossed tattoo machines with silver wings"></div>

    <h2 class="appt-heading">Appointment With</h2>
    <div class="appt-line"></div>

    <div class="field field--date"><span class="field-label">Date</span><span class="field-line"></span></div>
    <div class="field field--time"><span class="field-label">Time</span><span class="field-line"></span></div>
    <div class="field field--quote"><span class="field-label">Quote</span><span class="field-line"></span></div>
    <div class="field field--deposit"><span class="field-label">Deposit</span><span class="field-line"></span></div>

    <div class="social-mark" role="img" aria-label="Social page"></div>

    <p class="contact phone">(231)472-9035</p>
    <div class="rule rule--top"></div>
    <p class="contact address">2837 WEXLEY AVE. MUSKEGON, MI. 49517</p>
    <div class="rule rule--bottom"></div>
    <p class="contact website">WWW.INKRIDGEPARLOR.COM</p>
  </main>
</body>
</html>
```